WordPress WEB DESIGN & CODING for www.quellbrook-rigging.com Wireless Tower Contruction

WEB DESIGN & CODING for www.quellbrook-rigging.com
Wireless Tower Contruction Industry

SLOGAN: SERVICE AT A HIGHER LEVEL

Pardune Masts LLC has been in business since 2014 with combined professional Team experience of over 40 years.

Our Team is composed of long-time industry professionals in every aspect of the wireless telecommunications and commercial construction industries, including project management and site acquisition.

Pardune Masts specializes in providing tower installation services for the Wireless Telecommunications in the Southeastern of the United States.

Our key services are Wireless Tower Construction, Installation & Maintenance

Site audits and Tower mapping
Mount swaps and Modifications
Hardline & Jumper Installation
Antenna & Radio Install, Decom, Testing and Maintenance
Tower Lighting Installation & Testing
Fiber / Sweep / RET/ PIM Testing
Small Cells
Civil installation (concrete/steel platforms/electrical)
____________________________________________________________________

we need a clean yet vibrant, energetic website design that will convey our tower installation work to the fullest... It should use the navy and green colors of our logo and it must be mobile friendly and coded for both Android & IOS;
the site structure:
HOME
ABOUT
SERVICES
CONTRACT
CAREERS
GALLERY

I also attach a few pics we bought on pixgranary so these can be used if needed as we own them...

Target Market(s)

Client: large companies looking for general contractor or installation contractor in the market

Industry/Entity Type

Wireless Communication

Coding

Coded - Design and coding required

Number of Pages Required

4 page

Font styles to use
Sans Serif

Colors
0555a3
00a990
ffffff

Requirements
Must have
• Wordpress - must be both desktop mobile friendly and mobile is the key -
• should open swiftly on both Android & iOS
• See power point file with presentation about the company; page 5 is our keyservices but other contents can be used too
Nice to have
• panorama pics changing from the height/tower view showing the full overview, could be a slideshow or a short video...
Should not have
• flash animation does not work on iOS so this should be avoided.

```html
<!DOCTYPE html>
<html lang="en">
<head>
<meta charset="utf-8">
<title>Pardune Masts – Service at a Higher Level</title>
<link rel="stylesheet" href="https://fonts.googleapis.com/css2?family=Crimson+Pro:wght@500;600&family=Source+Sans+3:wght@400;600;700&display=swap">
<style>
:root{
  --navy:#2e2585;
  --sky:#6fa7de;
  --green:#3a8c2b;
  --ink:#1b1b1b;
  --text:#4a4a4a;
  --white:#ffffff;
  --serif:'Crimson Pro', Georgia, serif;
  --sans:'Source Sans 3', Arial, sans-serif;
}
*{box-sizing:border-box;margin:0;padding:0}
html,body{width:1200px;height:3854px;overflow:hidden;background:var(--white)}
body{position:relative;font-family:var(--sans);color:var(--text)}
.abs{position:absolute}
.btn{position:absolute;display:flex;align-items:center;justify-content:center;background:var(--green);color:var(--white);font-family:var(--serif);font-size:19px;font-weight:500;letter-spacing:.5px;border-radius:0 26px 26px 26px}
.heading{position:absolute;left:0;width:1200px;text-align:center;font-family:var(--serif);font-weight:600;color:var(--navy);font-size:42px}
.photo{position:absolute;border-radius:0 48px 0 0}
/* header */
.brand{left:78px;top:14px;display:flex;align-items:center;gap:10px;font-family:var(--serif);font-weight:600;font-size:26px;color:var(--green)}
.brand-dot{width:14px;height:14px;border-radius:50%;background:var(--navy)}
.nav{top:38px;left:0;font-size:14px;color:var(--white);text-transform:uppercase}
.nav span{position:absolute;white-space:nowrap}
.nav-active{position:absolute;left:500px;top:26px;width:36px;height:36px;border-radius:50%;background:var(--green)}
.nav-cta{left:998px;top:25px;width:124px;height:42px;border-radius:22px;font-size:18px}
.slider-dot{position:absolute;left:1158px;width:12px;height:12px;border-radius:50%;background:#d3d3e3}
.slider-dot.on{background:var(--green);border:2px solid #fff;box-shadow:0 0 0 1px var(--green)}
.hero-title{left:93px;top:288px;font-family:var(--serif);font-weight:500;font-size:55px;line-height:57px;color:var(--ink)}
.hero-text{left:95px;top:414px;width:420px;font-size:16px;line-height:27px;color:#222}
/* welcome */
.section-dot{left:588px;top:664px;width:24px;height:24px;border-radius:50%;background:var(--green)}
.about-text{left:633px;top:848px;width:370px;font-size:16px;line-height:27px}
.about-text p+p{margin-top:16px}
/* services */
.svc{position:absolute;width:220px;text-align:center}
.svc-icon{width:94px;height:94px;border-radius:50%;background:var(--green);margin:0 auto;display:flex;align-items:center;justify-content:center}
.svc h3{font-family:var(--serif);font-weight:600;color:var(--navy);font-size:21px;line-height:25px;margin-top:20px}
.svc p{font-size:15px;line-height:26px;color:var(--text);margin-top:12px}
.svc-arrow{margin:10px auto 0;display:block}
/* specialize */
.spec-title{left:124px;top:1722px;font-family:var(--serif);font-weight:600;font-size:42px;color:var(--navy)}
.spec-list{left:133px;top:1804px;list-style:none}
.spec-list li{display:flex;align-items:center;gap:18px;height:37.4px;font-size:16px;color:#333}
/* gallery */
.sub{position:absolute;left:0;width:1200px;text-align:center;font-size:15px;line-height:27px;color:var(--text)}
/* newsletter */
.email-field{left:284px;top:3360px;width:471px;height:53px;border-radius:27px;box-shadow:0 2px 10px rgba(0,0,0,.1);display:flex;align-items:center;justify-content:space-between;padding:0 24px;font-size:14px;color:#555}
/* footer */
.footer-disc{left:285px;top:3546px;width:630px;height:630px;border-radius:50%;background:var(--navy)}
.footer-badge{left:545px;top:3493px;width:110px;height:110px;border-radius:50%;background:var(--green);border:4px solid #fff;display:flex;align-items:center;justify-content:center;color:#fff;font-family:var(--serif);font-weight:600;font-size:17px;text-align:center;line-height:18px}
.social{position:absolute;top:3634px;width:42px;height:42px;border-radius:50%}
.foot-line{position:absolute;left:0;width:1200px;text-align:center;color:var(--white)}
</style>
</head>
<body>

<!-- Hero -->
<svg class="abs" style="left:0;top:0" width="1200" height="700" role="img" aria-label="Photo of a red and white lattice telecom tower against a blue sky">
  <defs>
    <linearGradient id="heroSky" x1="0" y1="0" x2="0.4" y2="1">
      <stop offset="0" stop-color="#2e2585"/>
      <stop offset="0.45" stop-color="#4a6ec4"/>
      <stop offset="1" stop-color="#7fb4e6"/>
    </linearGradient>
  </defs>
  <circle cx="733" cy="419" r="97" fill="var(--green)"/>
  <path d="M427 0 C 440 120, 520 200, 640 250 C 720 290, 700 420, 760 520 C 840 650, 1000 690, 1200 660 L1200 0 Z" fill="url(#heroSky)"/>
</svg>

<div class="abs brand"><span class="brand-dot"></span>Pardune Masts</div>

<div class="nav-active"></div>
<nav class="abs nav">
  <span style="left:521px">Home</span>
  <span style="left:591px">About</span>
  <span style="left:659px">Services</span>
  <span style="left:742px">Contract</span>
  <span style="left:834px">Careers</span>
  <span style="left:913px">Gallery</span>
</nav>
<div class="btn nav-cta">CONTACT</div>

<span class="slider-dot" style="top:313px"></span>
<span class="slider-dot on" style="top:334px"></span>
<span class="slider-dot" style="top:355px"></span>
<span class="slider-dot" style="top:376px"></span>
<span class="slider-dot" style="top:397px"></span>

<h1 class="abs hero-title">SERVICE AT A<br>HIGHER LEVEL</h1>
<p class="abs hero-text">Lorem Ipsum is simply dummy text of the printing and typesetting industry Lorem Ipsum.</p>
<div class="btn" style="left:93px;top:488px;width:177px;height:51px">CONTACT US</div>

<!-- Welcome -->
<div class="abs section-dot"></div>
<h2 class="heading" style="top:720px">Welcome To Pardune Masts</h2>

<div class="abs" style="left:-135px;top:890px;width:450px;height:450px;border-radius:50%;background:var(--navy)" role="img" aria-label="Navy-tinted photo of a steel tower seen from below"></div>
<div class="photo" style="left:212px;top:812px;width:365px;height:370px;background:linear-gradient(160deg,#3e5f8e 0%,#a9b8c9 45%,#eef1f4 60%,#5b6f85 100%)" role="img" aria-label="Photo of a lattice tower silhouetted against sun rays through clouds"></div>

<div class="abs about-text">
  <p>Pardune Masts LLC has been in business since 2014 with combined professional Team experience of over 40 years.</p>
  <p>Our Team is composed of long-time industry professionals in every aspect of the wireless telecommunications and commercial construction industries, including project management and site acquisition.</p>
</div>
<div class="btn" style="left:636px;top:1105px;width:177px;height:51px">LEARN MORE</div>

<!-- Services -->
<h2 class="heading" style="top:1276px">Our Services</h2>

<div class="svc" style="left:239px;top:1367px">
  <div class="svc-icon"><svg width="48" height="48" viewBox="0 0 48 48" fill="none" stroke="#fff" stroke-width="2"><path d="M8 44h32M14 44V30h8v14M18 30V18l10-8 6 6-8 6v8"/><circle cx="28" cy="10" r="3"/></svg></div>
  <h3>Installation</h3>
  <p>Lorem Ipsum is simply dummy text of the printing &amp; type setting industry.</p>
  <svg class="svc-arrow" width="28" height="12" viewBox="0 0 28 12"><path d="M0 6h22M18 1l7 5-7 5" stroke="var(--green)" stroke-width="2.5" fill="none"/></svg>
</div>
<div class="svc" style="left:488px;top:1367px">
  <div class="svc-icon"><svg width="48" height="48" viewBox="0 0 48 48" fill="none" stroke="#fff" stroke-width="2"><path d="M24 18l-9 26M24 18l9 26M17 38h14M19 30h10"/><circle cx="24" cy="16" r="3"/><path d="M17 10a10 10 0 0 1 14 0M13 6a16 16 0 0 1 22 0"/></svg></div>
  <h3>Wireless Tower<br>Construction</h3>
  <p>Lorem Ipsum is simply dummy text of the printing &amp; type setting industry.</p>
  <svg class="svc-arrow" width="28" height="12" viewBox="0 0 28 12"><path d="M0 6h22M18 1l7 5-7 5" stroke="var(--green)" stroke-width="2.5" fill="none"/></svg>
</div>
<div class="svc" style="left:730px;top:1367px">
  <div class="svc-icon"><svg width="48" height="48" viewBox="0 0 48 48" fill="none" stroke="#fff" stroke-width="2"><path d="M14 6v8l-4 4v24h8V18l-4-4M32 6h6v10h-6zM35 16v26"/></svg></div>
  <h3>Maintenance</h3>
  <p>Lorem Ipsum is simply dummy text of the printing &amp; type setting industry.</p>
  <svg class="svc-arrow" width="28" height="12" viewBox="0 0 28 12"><path d="M0 6h22M18 1l7 5-7 5" stroke="var(--green)" stroke-width="2.5" fill="none"/></svg>
</div>

<!-- Specialize -->
<h2 class="abs spec-title">Specialize In</h2>
<ul class="abs spec-list">
  <li><svg width="12" height="14" viewBox="0 0 12 14"><path d="M2 1l8 6-8 6" stroke="var(--green)" stroke-width="2.5" fill="none"/></svg>Site audits and Tower mapping</li>
  <li><svg width="12" height="14" viewBox="0 0 12 14"><path d="M2 1l8 6-8 6" stroke="var(--green)" stroke-width="2.5" fill="none"/></svg>Mount swaps and Modifications</li>
  <li><svg width="12" height="14" viewBox="0 0 12 14"><path d="M2 1l8 6-8 6" stroke="var(--green)" stroke-width="2.5" fill="none"/></svg>Hardline &amp; Jumper Installation</li>
  <li><svg width="12" height="14" viewBox="0 0 12 14"><path d="M2 1l8 6-8 6" stroke="var(--green)" stroke-width="2.5" fill="none"/></svg>Antenna &amp; Radio Install, Decom, Testing and Maintenance</li>
  <li><svg width="12" height="14" viewBox="0 0 12 14"><path d="M2 1l8 6-8 6" stroke="var(--green)" stroke-width="2.5" fill="none"/></svg>Tower Lighting Installation &amp; Testing</li>
  <li><svg width="12" height="14" viewBox="0 0 12 14"><path d="M2 1l8 6-8 6" stroke="var(--green)" stroke-width="2.5" fill="none"/></svg>Fiber / Sweep / RET/ PIM Testing</li>
  <li><svg width="12" height="14" viewBox="0 0 12 14"><path d="M2 1l8 6-8 6" stroke="var(--green)" stroke-width="2.5" fill="none"/></svg>Tower Lighting Installation &amp; Testing</li>
  <li><svg width="12" height="14" viewBox="0 0 12 14"><path d="M2 1l8 6-8 6" stroke="var(--green)" stroke-width="2.5" fill="none"/></svg>Small Cells</li>
  <li><svg width="12" height="14" viewBox="0 0 12 14"><path d="M2 1l8 6-8 6" stroke="var(--green)" stroke-width="2.5" fill="none"/></svg>Civil installation</li>
</ul>
<div class="btn" style="left:133px;top:2150px;width:177px;height:51px">CONTACT US</div>

<div class="abs" style="left:860px;top:1850px;width:434px;height:434px;border-radius:50%;background:var(--navy)" role="img" aria-label="Navy-tinted photo looking up inside a steel tower"></div>
<div class="photo" style="left:655px;top:1728px;width:365px;height:459px;background:linear-gradient(170deg,#5a7fb4 0%,#c9d6e6 45%,#8fa6c6 100%)" role="img" aria-label="Photo of a cellular antenna tower under a cloudy sky"></div>

<!-- Gallery -->
<h2 class="heading" style="top:2320px">Our Gallery</h2>
<p class="sub" style="top:2385px">Lorem Ipsum is simply dummy text of the printing &amp; type setting industry<br>Simply dummy text of the printing &amp; type.</p>

<div class="photo" style="left:174px;top:2473px;width:271px;height:312px;background:#5ba24a;display:flex;align-items:center;justify-content:center" role="img" aria-label="Photo of technicians working on a rooftop mast, shown with green overlay">
  <svg width="54" height="54" viewBox="0 0 54 54" fill="none" stroke="#fff" stroke-width="1.5"><circle cx="27" cy="27" r="25"/><circle cx="25" cy="25" r="7"/><path d="M30 30l6 6M25 22v6M22 25h6"/></svg>
</div>
<div class="photo" style="left:465px;top:2473px;width:271px;height:312px;background:linear-gradient(180deg,#2f7fd0,#6fb0ea)" role="img" aria-label="Photo of a white monopole cell tower against blue sky"></div>
<div class="photo" style="left:757px;top:2473px;width:271px;height:312px;background:linear-gradient(180deg,#5d86c7 0%,#8fb2e0 70%,#6b8a3a 88%,#4c6a2a 100%)" role="img" aria-label="Photo of red and white towers above green trees"></div>
<div class="photo" style="left:174px;top:2806px;width:271px;height:312px;background:linear-gradient(180deg,#3c7fcf 0%,#9cc3ea 65%,#2f4a2a 100%)" role="img" aria-label="Photo of a monopole tower rising above pine trees"></div>
<div class="photo" style="left:465px;top:2806px;width:271px;height:312px;background:linear-gradient(180deg,#6f9fd6,#cfe0f2)" role="img" aria-label="Photo of a climber in safety gear at a white pole"></div>
<div class="photo" style="left:757px;top:2806px;width:271px;height:312px;background:linear-gradient(180deg,#b8d3f2,#4f7ed0)" role="img" aria-label="Photo of a blue antenna mast against bright sky"></div>

<div class="btn" style="left:501px;top:3145px;width:198px;height:50px">EXPLORE MORE</div>

<!-- Newsletter -->
<h2 class="heading" style="top:3250px">Sign Up For Newsletter !</h2>
<p class="sub" style="top:3312px;font-size:14px">Would you like to receive any Exclusive Update For SignUp Our Newsletter !</p>
<div class="abs email-field"><span>Enter Email *</span>
  <svg width="16" height="12" viewBox="0 0 16 12"><rect x="0.5" y="0.5" width="15" height="11" fill="#bbb"/><path d="M1 1l7 6 7-6" stroke="#fff" fill="none"/></svg>
</div>
<div class="btn" style="left:769px;top:3360px;width:156px;height:52px">SUBSCRIBE</div>

<!-- Footer -->
<div class="abs footer-disc"></div>
<div class="abs footer-badge">Pardune<br>Masts</div>
<span class="social" style="left:532px;background:#1f5fb8"></span>
<span class="social" style="left:579px;background:#1ea1e6"></span>
<span class="social" style="left:625px;background:#d2412f"></span>
<p class="foot-line" style="top:3695px;font-size:26px;font-weight:700">555 014 2290</p>
<p class="foot-line" style="top:3731px;font-size:18px">info@pardunemasts.com</p>
<p class="foot-line" style="top:3786px;font-size:14px">©Pardune Masts - 2019 All Rights Reserved.</p>

</body>
</html>
```